We need a business card and letterhead design for an orthodontic office. Needs to be clean, simple and sleek

Target Market(s)

adults/children

Industry/Entity Type

Dental

Contact Information for Business Card

Logo that is attached

Font styles to use
Serif

Colors

Designer to choose colors to be used in the design.

Requirements
Must have
• Martin L Okrand DDS
• Corinne Vesta DMD
• 82 Tolliver Avenue
• Dunwick,NY 11874
• (516) 472-9054
• www.okrandortho.example
Nice to have
• on the back.... space for appointment times
Should not have
• teeth

```html
<!DOCTYPE html>
<html lang="en">
<head>
<meta charset="utf-8">
<title>Okrand Orthodontics – Business Card</title>
<link href="https://fonts.googleapis.com/css2?family=Open+Sans:wght@400;600;700&display=swap" rel="stylesheet">
<style>
  :root {
    --charcoal: #2d2d2e;
    --ink: #222226;
    --sky: #5aa3cf;
    --paper: #ffffff;
    --backdrop: #ecebe8;
    --front-text: #f2f2f2;
  }
  * { margin: 0; padding: 0; box-sizing: border-box; }
  html, body { width: 1200px; height: 900px; overflow: hidden; }
  body {
    background: var(--backdrop);
    font-family: "Open Sans", Arial, sans-serif;
    display: flex;
    flex-direction: column;
    align-items: center;
    justify-content: center;
    gap: 56px;
  }
  .card {
    position: relative;
    width: 640px;
    height: 366px;
    overflow: hidden;
    box-shadow: 0 4px 14px rgba(0,0,0,0.15);
  }
  .card--front { background: var(--charcoal); }
  .card--back { background: var(--paper); }

  .brand-name {
    position: absolute;
    display: flex;
    align-items: center;
    gap: 12px;
    font-weight: 600;
    line-height: 1.2;
  }
  .brand-name .dot {
    flex: none;
    border-radius: 50%;
    background: currentColor;
  }
  .card--front .brand-name {
    left: 220px;
    top: 110px;
    color: var(--front-text);
    font-size: 32px;
  }
  .card--front .brand-name .dot { width: 22px; height: 22px; }
  .card--back .brand-name {
    right: 34px;
    top: 44px;
    color: var(--ink);
    font-size: 26px;
  }
  .card--back .brand-name .dot { width: 18px; height: 18px; }

  .practitioners {
    position: absolute;
    left: 34px;
    top: 50px;
    list-style: none;
    font-size: 17px;
    font-weight: 600;
    color: var(--sky);
    line-height: 1.5;
    text-transform: uppercase;
  }
  .practitioners .degree { color: var(--ink); font-weight: 700; }

  .contact {
    position: absolute;
    left: 62px;
    top: 188px;
    font-size: 15px;
    color: var(--ink);
    line-height: 1.4;
    font-style: normal;
  }
  .contact .line { display: flex; align-items: center; gap: 7px; }
  .contact svg { width: 12px; height: 12px; fill: var(--sky); }

  .swoosh { position: absolute; inset: 0; width: 640px; height: 366px; }
</style>
</head>
<body>

  <section class="card card--front" aria-label="Card front">
    <div class="brand-name"><span class="dot"></span><span>Okrand<br>Orthodontics</span></div>
  </section>

  <section class="card card--back" aria-label="Card back">
    <svg class="swoosh" viewBox="0 0 640 366" aria-hidden="true">
      <path d="M0,345 C200,392 440,335 640,165 L640,366 L0,366 Z" fill="var(--charcoal)"/>
      <path d="M0,316 C200,372 420,318 565,214 C425,340 200,384 0,334 Z" fill="var(--sky)"/>
    </svg>

    <ul class="practitioners">
      <li>Martin L Okrand <span class="degree">DDS</span></li>
      <li>Corinne Vesta <span class="degree">DMD</span></li>
    </ul>

    <div class="brand-name"><span class="dot"></span><span>Okrand<br>Orthodontics</span></div>

    <address class="contact">
      <div>82 Tolliver Avenue</div>
      <div>Dunwick,NY 11874</div>
      <div class="line">
        <svg viewBox="0 0 24 24"><path d="M6.6 10.8a15.1 15.1 0 0 0 6.6 6.6l2.2-2.2c.3-.3.7-.4 1-.2 1.1.4 2.3.6 3.6.6.6 0 1 .4 1 1V20c0 .6-.4 1-1 1A17 17 0 0 1 3 4c0-.6.4-1 1-1h3.5c.6 0 1 .4 1 1 0 1.3.2 2.5.6 3.6.1.3 0 .7-.2 1z"/></svg>
        <span>(516) 472-9054</span>
      </div>
      <div class="line">
        <svg viewBox="0 0 24 24"><circle cx="12" cy="12" r="10"/></svg>
        <span>www.okrandortho.example</span>
      </div>
    </address>
  </section>

</body>
</html>
```